Resume build

I need someone to develop a resume for me. This needs to include a stylized template as well as improving the content of my existing resume.
Updates

All content generated. Just need resume to be formatted and stylized a few different options. With offer a few different head shots to go into it as well. Final versions to be in PDF.

Target Market(s)

this is not for finding a job but is for presenting to clients on who I am and why I'm the qualified candidate to perform their work.

Industry/Entity Type

Marine

Colors
0054AA
0677BA
7BADD7
CADEEF
E8F1F8

Requirements
Must have
• must be in PDF and have a location to add a picture later in the top corner

```html
<!DOCTYPE html>
<html lang="en">
<head>
<meta charset="utf-8">
<title>Callum Hartley – Resume</title>
<link href="https://fonts.googleapis.com/css2?family=Montserrat:ital,wght@0,400;0,500;0,600;0,700;0,800;1,700&display=swap" rel="stylesheet">
<style>
:root{
  --navy:#0054AA;
  --blue:#0677BA;
  --sky:#7BADD7;
  --mist:#CADEEF;
  --ice:#E8F1F8;
  --ink:#2b2f38;
  --paper:#ffffff;
  --backdrop:#ececef;
}
*{box-sizing:border-box;margin:0;padding:0}
html,body{width:1200px;height:800px;overflow:hidden;background:var(--backdrop);font-family:'Montserrat',sans-serif;color:var(--ink)}
.resume{position:absolute;left:324px;top:10px;width:552px;height:780px;background:var(--paper);box-shadow:0 2px 10px rgba(0,0,0,.12);overflow:hidden}
.resume::after{content:"";position:absolute;left:0;right:0;bottom:10px;height:2px;background:var(--navy)}

/* sidebar */
.profile{position:absolute;left:0;top:0;width:218px;height:292px;background:var(--navy);border-radius:0 0 16px 0;padding:16px 16px 0}
.headshot{width:184px;height:170px;border-radius:14px;background:linear-gradient(160deg,#5b6068,#2c3038 70%,#1c2a44)}
.profile-name{margin-top:12px;color:#fff;font-weight:800;font-size:22px;letter-spacing:.2px}
.contact{list-style:none;margin-top:7px}
.contact li{display:flex;align-items:flex-start;gap:7px;color:#fff;font-size:7.4px;line-height:1.35;margin-bottom:5px}
.contact svg{flex:none;width:12px;height:12px}
.tagline{position:absolute;left:18px;top:302px;width:190px;color:var(--navy);font-weight:700;font-style:italic;font-size:9.4px;line-height:1.35;text-decoration:underline;text-underline-offset:2px}

.side-box{position:absolute;left:18px;width:196px;background:var(--mist);border-radius:12px;padding:26px 12px 12px}
.education{top:340px;height:112px}
.certifications{top:462px;height:306px;background:linear-gradient(var(--mist),var(--ice))}
.pill{position:absolute;left:-4px;top:-2px;background:var(--navy);color:#fff;font-weight:800;font-size:10.5px;padding:5px 12px;border-radius:0 12px 12px 12px;letter-spacing:.3px}
.edu-item{position:relative;padding-left:12px;margin-bottom:8px;font-size:6.6px;line-height:1.35}
.edu-item b{font-weight:700;font-size:7px}
.edu-year{position:absolute;right:0;top:-9px;font-weight:700;font-size:7px;color:var(--ink)}
.ring{position:absolute;left:0;top:2px;width:6px;height:6px;border:1.3px solid var(--navy);border-radius:50%}
.cert-list{list-style:none;border-left:1px dotted var(--navy);margin-left:3px;padding-top:4px}
.cert-list li{position:relative;padding-left:10px;font-size:7px;line-height:1.35;margin-bottom:6.5px}
.cert-list li::before{content:"";position:absolute;left:-4px;top:2px;width:6px;height:6px;border:1.3px solid var(--navy);border-radius:50%;background:var(--mist)}

/* experience */
.experience{position:absolute;left:232px;top:14px;width:306px}
.section-title{color:var(--navy);font-weight:800;font-size:17px;letter-spacing:.3px;border-bottom:1px solid var(--blue);padding-bottom:1px;margin-bottom:4px}
.job{position:relative;margin-bottom:7px}
.job-date{position:absolute;right:0;top:-11px;color:var(--navy);font-weight:700;font-style:italic;font-size:7.4px}
.job-role{color:var(--navy);font-weight:700;font-size:7.6px;line-height:1.25}
.duties{list-style:none;margin:3px 0 0 3px;border-left:1px dotted var(--navy)}
.duties li{position:relative;padding-left:10px;font-size:6.7px;line-height:1.33;margin-bottom:1.5px}
.duties li::before{content:"";position:absolute;left:-4px;top:2px;width:6px;height:6px;border:1.3px solid var(--navy);border-radius:50%;background:#fff}
.job:first-of-type .job-date{top:-21px}
</style>
</head>
<body>
<main class="resume">
  <header class="profile">
    <div class="headshot" role="img" aria-label="Headshot photo placeholder"></div>
    <h1 class="profile-name">Callum Hartley</h1>
    <ul class="contact">
      <li><svg viewBox="0 0 12 12"><circle cx="6" cy="6" r="6" fill="#fff"/><path d="M6 2.6a2.2 2.2 0 0 0-2.2 2.2C3.8 6.5 6 9.2 6 9.2s2.2-2.7 2.2-4.4A2.2 2.2 0 0 0 6 2.6z" fill="#0054AA"/><circle cx="6" cy="4.8" r=".8" fill="#fff"/></svg><span>402 Harbourview Lane<br>Victoria, BC Canada V8X 1A1</span></li>
      <li><svg viewBox="0 0 12 12"><circle cx="6" cy="6" r="6" fill="#fff"/><path d="M4 3h1.2l.6 1.6-.8.6a4 4 0 0 0 1.8 1.8l.6-.8 1.6.6V8a1 1 0 0 1-1 1A5 5 0 0 1 3 4a1 1 0 0 1 1-1z" fill="#0054AA"/></svg><span>1 (604) 555 0182</span></li>
      <li><svg viewBox="0 0 12 12"><circle cx="6" cy="6" r="6" fill="#fff"/><rect x="3" y="4" width="6" height="4.2" rx=".5" fill="#0054AA"/><path d="M3.2 4.3 6 6.4l2.8-2.1" stroke="#fff" stroke-width=".6" fill="none"/></svg><span>callum@tidelinemarine.com</span></li>
    </ul>
  </header>

  <p class="tagline">A proven expert in marine project management and operation</p>

  <section class="side-box education">
    <h2 class="pill">EDUCATION</h2>
    <div class="edu-item"><span class="ring"></span><span class="edu-year">2004 - 2008</span><b>Nautical Sciences Degree</b><br>Pacific Institute of Technology<br>North Vancouver, British Columbia</div>
    <div class="edu-item"><span class="ring"></span><span class="edu-year">2001 - 2003</span><b>Associate of Arts Degree</b><br>Westbrook College<br>Vancouver, British Columbia</div>
  </section>

  <section class="side-box certifications">
    <h2 class="pill">CERTIFICATIONS &amp; SKILLS</h2>
    <ul class="cert-list">
      <li>Master Mariner</li>
      <li>Certificate in the Fundamentals of Liquefied Natural Gas, Harbourline Maritime Academy</li>
      <li>Incident Command Training 100</li>
      <li>Bridge Resource Management Certificate</li>
      <li>Ship Security Officer</li>
      <li>Basic Tanker Safety Certificate</li>
      <li>Basic Safety Training</li>
      <li>Marine Advanced Firefighting</li>
      <li>Marine Emergency Duties Senior Officer</li>
      <li>Proficiency in Survival Craft Certificate</li>
      <li>General Operators GMDSS Certificate</li>
      <li>Fast Rescue Craft Certificate</li>
      <li>Marine Advanced First Aid</li>
    </ul>
  </section>

  <section class="experience">
    <h2 class="section-title">EXPERIENCE</h2>

    <article class="job">
      <span class="job-date">2015 - Present</span>
      <h3 class="job-role">Tideline Marine Ltd., Co-Founder/Managing Director<br>Victoria, British Columbia</h3>
      <ul class="duties">
        <li>Manage complex multi-million-dollar marine projects from inception through to execution</li>
        <li>Guide clients through regulatory processes with marine government regulators</li>
        <li>Represent owners in new vessel construction and refit projects globally</li>
        <li>Supply and operate passenger vessels for custom client projects</li>
        <li>Design &amp; implementation of national marine regulator approved Safety Management Systems</li>
        <li>Advise clients through marine start-ups and business planning</li>
        <li>Supply personnel to various marine operators globally as needed</li>
      </ul>
    </article>

    <article class="job">
      <span class="job-date">2019 - 2021</span>
      <h3 class="job-role">Pacific Coast Ferries, Senior Manager, Nautical Standards<br>Victoria, British Columbia</h3>
      <ul class="duties">
        <li>Manages the procurement, implementation and life-cycle management of fleet-wide deck department safety critical assets &amp; navigational equipment for fleet of 38 vessels</li>
        <li>Chairs the Nautical Standards Committee and Vessel Electronics Program that oversees the selection and implementation of fleet equipment</li>
        <li>Works with the Fleet Technical and Vessel Replacement divisions in the selection process for new major equipment</li>
        <li>Advises on design and equipment profiles for new vessel construction</li>
        <li>Develops new initiatives to ensure vessel performance and readiness</li>
      </ul>
    </article>

    <article class="job">
      <span class="job-date">2017 - 2019</span>
      <h3 class="job-role">Pacific Coast Ferries, Senior Captain<br>South Coast, British Columbia</h3>
      <ul class="duties">
        <li>Captain and vessel manager</li>
        <li>Responsible for overall operation of the vessel including navigation, budgeting, labour, safety management, regulatory compliance, deck maintenance &amp; training</li>
        <li>Responsible for up to 30 crew/staff</li>
      </ul>
    </article>

    <article class="job">
      <span class="job-date">2013 - 2017</span>
      <h3 class="job-role">Coastal Marine Search &amp; Rescue, Safety Manager<br>Victoria, British Columbia</h3>
      <ul class="duties">
        <li>Implemented a provincial wide safety management program for marine search and rescue</li>
        <li>Managed a five-member safety team representing various regions across the province</li>
        <li>Drafted and issued new policies including Standard Operating Procedures, Annual Vessel Inspections, Vessel Familiarizations &amp; Planned Vessel Maintenance</li>
      </ul>
    </article>

    <article class="job">
      <span class="job-date">2012 - 2016</span>
      <h3 class="job-role">Westgate Port Authority, Operations Coordinator<br>Vancouver, British Columbia</h3>
      <ul class="duties">
        <li>Oversaw the safe and efficient operations of marine activity within the port's jurisdiction acting as the Harbour Masters representative</li>
        <li>Responded to marine, land and security incidents, ensuring initial actions were taken by relevant parties</li>
        <li>Acted as the initial and primary means of communication between the port and external stakeholders, regulatory agencies and the public</li>
      </ul>
    </article>

    <article class="job">
      <span class="job-date">2008 - 2011</span>
      <h3 class="job-role">Meridian Cruises, Chief Officer<br>Folkestone, United Kingdom</h3>
      <ul class="duties">
        <li>Managed a 20-man deck department including 2 watch-keeping officers, 2 bosons and 16 able-bodied and ordinary seamen</li>
        <li>Held daily 4-8 watch in a single watch-keeping system conducting the majority of arrivals and departures in ports all over the world</li>
      </ul>
    </article>

    <article class="job">
      <span class="job-date">2004 - 2008</span>
      <h3 class="job-role">Various Vessels Operating Globally<br>Junior Navigational Officer</h3>
      <ul class="duties">
        <li>Responsibilities included: holding regular navigational watch, mooring stations, all official logbooks, chart corrections, lifeboat maintenance, meteorological observations and fire-fighting equipment maintenance</li>
      </ul>
    </article>
  </section>
</main>
</body>
</html>
```